Music CD Design Project - 4 panel

Pop rock / soft rock ballad single CD case artwork.
Female singer in her 20s.
Would like something clean, classic, cool, sexy.

4 panel gatefold card case - Template: http://www.duplimark.com.au/storage/duplimark-artwork-templates/Duplimark%20Gatefold%20Sleeve.pdf

Artwork specifications:
http://www.duplimark.com.au/artwork-cd-dvd-replication/

Target Market(s)

Record Labels & Commercial Radio Stations / Listeners

Industry/Entity Type

Singer

Requirements
Must have
• Must have all 4 panels utilised (Template: http://www.duplimark.com.au/storage/duplimark-artwork-templates/Duplimark%20Gatefold%20Sleeve.pdf )
Must have text included (below) :
_______________________________________________________
COVER TEXT
ROS KERROW
Hollowed

INSIDE TEXT

HOLLOWED
Performed by: Rosalind Kerrow
Written By: Rosalind Kerrow, Gregory J. Olsen, Hugh Lamb
Recorded in Sydney NSW, produced, engineered and mixed by Gregory J. Olsen. Drums: Laurent Vischorelle. Vocals recorded at Tidal Studio, Perth WA.

PAINTED RIVERS
Written By: Rosalind Kerrow, Gregory J. Olsen
Produced and Mixed: Gregory Olsen at Gregory Olsen Studio, Sydney, New South Wales. Drums: Laurent Vischorelle.

BACK TEXT
Track 1: Hollowed
Track 2: Hollowed [Radio Edit]
Track 3: Painted Rivers

www.RosKerrowMusic.com
Photography: Rosalind Ivy Photography / Bree Vantorre Photography
_____________________________________________________
I have attached photos please use whatever you think will suit.
Inside text can be small print, I just need it there but doesn't have to be the feature / main item.
Nice to have
• LYRICS

HOLLOWED
You're in my picture frame / In black and white before the night you went away / I can't forget that day / My heart I heart it break / Like glass it fell and shattered silently / Your words cut violently / Left me to bleed / Stripped bare of my innocence / Your scent lingers on me / Sounds of an ambulance as my heart it screams / I wished for a nightmare / I prayed for the sun / Not even its warmth could heal me / And it's HOLLOWED to wish upon a star / HOLLOWED to wonder where you are / HOLLOWED I gotta change my tune / It's HOLLOWED I'm not wasting my time on you / Here comes another moon / Tell me how many nights did I cry for you / These tears of truth / Sunrise to sunsets I still remain / A prisoner to my bed for days, afraid / Because life is a maze without you / I taste the tears along my lips / Stuck in this solar eclipse / The day will end without my best friend / I wished for a nightmare / I prayed for the sun / Not even its warmth could heal me / And it's HOLLOWED to wish upon a star / HOLLOWED to wonder where you are / HOLLOWED I gotta change my tune / It's HOLLOWED I'm not wasting my time on you / Here comes another moon / Tell me how many nights did I cry for you / These tears of truth / Sunrise to sunsets I still remain / A prisoner to my bed for days, afraid / Because life is a maze without you / And it's HOLLOWED to wish upon a star / HOLLOWED to wonder where you are / HOLLOWED I gotta change my tune / It's HOLLOWED I'm not wasting my time on you.

PAINTED RIVERS
Hello Pinnochio, your other woman called / So cut your nose to spite your face / Your double mask will be defaced / Lying through your wooden teeth / Your puppet pants on fire / There's no real man underneath / You're one IMPRESSIVE LIAR / You think I'm blind, but I have eyes / I see right through your PAINTED RIVERS / The faith I had has now expired / Thrown out with your porky pies / This time I can't ignore I won't take it anymore / I'm calling your bluff cos I've had enough of your PAINTED RIVERS/ You're running late again, repeating that same old story / Improvisation of fiction, your compulsive addiction / Does nothing for me / Lost in a labyrinth of lies / Your tangled web on fire / Remembering every alibi / You're one IMPRESSIVE LIAR / You think I'm blind, but I have eyes / I see right through your PAINTED RIVERS / The faith I had has now expired / Thrown out with your porky pies / This time I can't ignore I won't take it anymore / I'm calling your bluff cos I've had enough of your PAINTED RIVERS / Words thrown around a thousand times / Promises are made and tossed aside / You think I'm wrapped around your finger / But I'm leaving you behind / You think I'm blind, but I have eyes / I see right through your PAINTED RIVERS / The faith I had has now expired / Thrown out with your porky pies / This time I can't ignore I won't take it anymore / I'm calling your bluff cos I've had enough of your IMPRESSIVE / I'm calling your bluff cos I've had enough of your PAINTED RIVERS

```html
<!DOCTYPE html>
<html lang="en">
<head>
<meta charset="utf-8">
<title>Ros Kerrow – Hollowed – Gatefold Sleeve</title>
<link href="https://fonts.googleapis.com/css2?family=Source+Sans+3:wght@400;600;700&display=swap" rel="stylesheet">
<style>
  :root{
    --paper:#ffffff;
    --ink:#2b2b2b;
    --dim-red:#e0232b;
    --guide:#b9b9b9;
    --bleed-green:#7cc47a;
    --spine-purple:#9b5fb0;
    --river-blue:#1ba1dc;
    --hollow-red:#e8222d;
    --cover-red:#e31b23;
    --panel-wash:rgba(255,255,255,.72);
  }
  *{box-sizing:border-box;margin:0;padding:0}
  html,body{width:1200px;height:575px;overflow:hidden;background:var(--paper)}
  body{position:relative;font-family:"Source Sans 3",Arial,sans-serif;color:var(--ink)}
  .artboard{position:absolute;inset:0}
  .dim-label{position:absolute;font-size:8px;color:var(--ink);transform:translateX(-50%)}
  .dim-label--v{transform:translateY(-50%)}
  .thumb-caption{position:absolute;font-size:4px;color:#555}
  .thumb-word{position:absolute;font-size:4px;font-weight:700;color:#333}

  .lyric-card{position:absolute;background:var(--panel-wash);border-radius:0 8px 0 0;overflow:hidden}
  .lyric-card__title{height:17px;color:#fff;font-weight:700;font-size:10.5px;line-height:17px;padding-left:6px;border-radius:0 8px 0 0;letter-spacing:.2px}
  .lyric-card__title--rivers{background:var(--river-blue)}
  .lyric-card__title--hollowed{background:var(--hollow-red)}
  .credits{padding:4px 6px 0;font-size:6.6px;line-height:7.4px}
  .credits--bold{font-weight:700}
  .lyrics{display:flex;gap:10px;padding:8px 6px 0;font-size:3.6px;line-height:4.3px;font-weight:600;color:#333}
  .lyrics__col{flex:1}
  .lyrics__col p{margin-bottom:4px}

  .track-list{position:absolute;left:450px;top:200px;width:102px;height:28px;border:1px solid #fff;border-radius:5px;color:#fff;font-size:6.6px;line-height:8px;padding:2px 0 0 6px;font-weight:600}
  .back-web{position:absolute;left:327px;top:381px;color:#fff;font-weight:700;font-size:9px}
  .back-photo{position:absolute;left:327px;top:391px;color:#fff;font-weight:700;font-size:6.8px}

  .cover-artist{position:absolute;left:573px;top:182px;color:var(--cover-red);font-weight:700;font-size:16px;letter-spacing:.3px}
  .cover-title{position:absolute;left:573px;top:196px;color:#3a3a3a;font-size:14px;font-weight:400}
</style>
</head>
<body>
<div class="artboard">
<svg width="1200" height="575" viewBox="0 0 1200 575" xmlns="http://www.w3.org/2000/svg">
  <defs>
    <linearGradient id="sunset-sea" x1="0" y1="120" x2="0" y2="447" gradientUnits="userSpaceOnUse">
      <stop offset="0" stop-color="#e39a3e"/>
      <stop offset=".28" stop-color="#f3c45a"/>
      <stop offset=".38" stop-color="#f8dd8a"/>
      <stop offset=".46" stop-color="#9c6b4a"/>
      <stop offset=".7" stop-color="#5e4a47"/>
      <stop offset="1" stop-color="#b57a3e"/>
    </linearGradient>
    <radialGradient id="portrait-tone" cx="700" cy="260" r="170" gradientUnits="userSpaceOnUse">
      <stop offset="0" stop-color="#e8cdb0"/>
      <stop offset=".55" stop-color="#d9b27a"/>
      <stop offset="1" stop-color="#f2ece4"/>
    </radialGradient>
    <linearGradient id="beach-tone" x1="0" y1="157" x2="0" y2="410" gradientUnits="userSpaceOnUse">
      <stop offset="0" stop-color="#8fb7cf"/>
      <stop offset=".35" stop-color="#cfd9d6"/>
      <stop offset=".6" stop-color="#e4cfa4"/>
      <stop offset="1" stop-color="#d8b27a"/>
    </linearGradient>
  </defs>

  <g class="template-thumb" fill="none" stroke="#9a9a9a" stroke-width=".5">
    <rect x="27" y="20" width="120" height="27"/>
    <line x1="57" y1="20" x2="57" y2="47"/><line x1="87" y1="20" x2="87" y2="47"/><line x1="117" y1="20" x2="117" y2="47"/>
    <line x1="20" y1="10" x2="150" y2="10"/>
  </g>
  <rect x="24" y="62" width="2" height="2" fill="#777"/>
  <rect x="34" y="62" width="2" height="2" fill="#777"/>

  <g class="dimensions" stroke="var(--dim-red)" stroke-width="1.2" fill="var(--dim-red)">
    <line x1="80" y1="95" x2="314" y2="95"/><path d="M77 95l6-3v6z M317 95l-6-3v6z" stroke="none"/>
    <line x1="322" y1="95" x2="556" y2="95"/><path d="M319 95l6-3v6z M559 95l-6-3v6z" stroke="none"/>
    <line x1="563" y1="95" x2="569" y2="95"/>
    <line x1="575" y1="95" x2="809" y2="95"/><path d="M572 95l6-3v6z M812 95l-6-3v6z" stroke="none"/>
    <line x1="820" y1="95" x2="1047" y2="95"/><path d="M817 95l6-3v6z M1050 95l-6-3v6z" stroke="none"/>
    <line x1="48" y1="124" x2="48" y2="443"/><path d="M48 120l-3 6h6z M48 447l-3-6h6z" stroke="none"/>
    <line x1="1075" y1="167" x2="1075" y2="401"/><path d="M1075 163l-3 6h6z M1075 405l-3-6h6z" stroke="none"/>
  </g>
  <g class="guides" stroke="var(--guide)" stroke-width=".6">
    <line x1="77" y1="86" x2="77" y2="104"/><line x1="317" y1="86" x2="317" y2="104"/>
    <line x1="559" y1="86" x2="559" y2="104"/><line x1="570" y1="86" x2="570" y2="104"/>
    <line x1="812" y1="86" x2="812" y2="104"/><line x1="1050" y1="86" x2="1050" y2="104"/>
    <line x1="38" y1="120" x2="62" y2="120"/><line x1="38" y1="447" x2="62" y2="447"/>
    <line x1="1062" y1="120" x2="1088" y2="120"/><line x1="1062" y1="163" x2="1088" y2="163"/>
    <line x1="1062" y1="405" x2="1088" y2="405"/><line x1="1062" y1="447" x2="1088" y2="447"/>
    <line x1="72" y1="466" x2="72" y2="490"/><line x1="313" y1="466" x2="313" y2="490"/>
    <line x1="560" y1="466" x2="560" y2="490"/><line x1="812" y1="466" x2="812" y2="490"/>
    <line x1="1050" y1="466" x2="1050" y2="490"/>
  </g>

  <path role="img" aria-label="Sunset over the sea, photograph area" d="M68 157 L317 157 L317 410 L68 410 Q112 283 68 157 Z" fill="url(#sunset-sea)"/>
  <path role="img" aria-label="Singer standing in the surf at sunset, photograph area" d="M317 157 L340 120 L538 120 L560 157 L560 410 L538 447 L340 447 L317 410 Z" fill="url(#sunset-sea)"/>
  <path d="M317 157 L340 120 L538 120 L560 157 M317 410 L340 447 L538 447 L560 410" fill="none" stroke="var(--spine-purple)" stroke-width=".6"/>
  <rect x="560" y="157" width="255" height="253" fill="#f3efea"/>
  <rect role="img" aria-label="Portrait of the singer with long blonde curls" x="600" y="157" width="215" height="253" fill="url(#portrait-tone)"/>
  <g stroke="var(--spine-purple)" stroke-width=".7">
    <line x1="560" y1="157" x2="560" y2="410"/><line x1="570" y1="157" x2="570" y2="410"/>
    <line x1="560" y1="405" x2="812" y2="405"/>
  </g>
  <rect role="img" aria-label="Singer on a sunny beach, photograph area" x="815" y="157" width="243" height="253" fill="url(#beach-tone)"/>
  <g fill="none" stroke="var(--bleed-green)" stroke-width=".8" stroke-dasharray="3 2">
    <line x1="68" y1="157" x2="317" y2="157"/>
    <line x1="560" y1="157" x2="1058" y2="157"/>
    <line x1="1058" y1="157" x2="1058" y2="410"/>
  </g>
</svg>

<span class="thumb-caption" style="left:20px;top:2px">Preview</span>
<span class="thumb-word" style="left:64px;top:31px">Back</span>
<span class="thumb-word" style="left:94px;top:31px">Front</span>
<span class="thumb-caption" style="left:28px;top:61px">Bleed Safe</span>

<span class="dim-label" style="left:197px;top:74px">124mm</span>
<span class="dim-label" style="left:438px;top:74px">126mm</span>
<span class="dim-label" style="left:565px;top:74px">4mm</span>
<span class="dim-label" style="left:692px;top:74px">127mm</span>
<span class="dim-label" style="left:933px;top:74px">122mm</span>
<span class="dim-label dim-label--v" style="left:19px;top:283px">169mm</span>
<span class="dim-label dim-label--v" style="left:1092px;top:283px">125mm</span>

<section class="lyric-card" style="left:105px;top:177px;width:202px;height:213px">
  <h2 class="lyric-card__title lyric-card__title--rivers">PAINTED RIVERS</h2>
  <div class="credits credits--bold">
    Performed by: Rosalind Kerrow<br>
    Written By: Rosalind Kerrow, Gregory J. Olsen<br>
    Produced and Mixed: Gregory Olsen at Gregory Olsen Studio, Sydney, New South Wales. Drums: Laurent Vischorelle.
  </div>
  <div class="lyrics">
    <div class="lyrics__col">
      <p>Hello stranger, your other lover phoned<br>So paint your smile another shade<br>Your borrowed mask is bound to fade<br>Talking through a painted grin<br>Your story's wearing thin<br>There's no one real within</p>
      <p>You run like PAINTED RIVERS<br>You think I'm lost, but I can see<br>The colours running into me<br>The trust I gave has washed away<br>Gone down with all you say<br>This time I close the door, I won't drift there anymore<br>I'm rowing to shore cos I've had enough of your PAINTED RIVERS</p>
      <p>You're turning up so late, retelling that tired tale<br>A canvas of excuses, every brushstroke useless<br>Means nothing to me<br>Lost in a current of your games<br>Your colours bleed and dry<br>Counting every alibi</p>
      <p>You run like PAINTED RIVERS<br>You think I'm lost, but I can see<br>The colours running into me<br>The trust I gave has washed away<br>Gone down with all you say<br>This time I close the door, I won't drift there anymore<br>I'm rowing to shore cos I've had enough of your PAINTED RIVERS</p>
    </div>
    <div class="lyrics__col">
      <p>Words spilled a hundred times<br>Promises drawn then washed aside<br>You think I'm tangled in your stream<br>But I'm leaving you behind<br>You think I'm lost, but I can see</p>
      <p>The colours running into me<br>The trust I gave has washed away<br>Gone down with all you say<br>This time I close the door, I won't drift there anymore<br>I'm rowing to shore cos I've had enough of your colours<br>I'm rowing to shore cos I've had enough of your PAINTED RIVERS</p>
    </div>
  </div>
</section>

<div class="track-list">Track 1: Hollowed<br>Track 2: Hollowed [Radio Edit]<br>Track 3: Painted Rivers</div>
<div class="back-web">www.RosKerrowMusic.com</div>
<div class="back-photo">Photography: Rosalind Ivy Photography / Bree Vantorre Photography</div>

<h1 class="cover-artist">ROS KERROW</h1>
<div class="cover-title">Hollowed</div>

<section class="lyric-card" style="left:825px;top:175px;width:218px;height:215px">
  <h2 class="lyric-card__title lyric-card__title--hollowed">HOLLOWED</h2>
  <div class="credits">
    Performed by: Rosalind Kerrow<br>
    Written By: Rosalind Kerrow, Gregory J. Olsen, Hugh Lamb<br>
    Recorded in Sydney NSW, produced, engineered and mixed by Gregory J. Olsen. Drums: Laurent Vischorelle. Vocals recorded at Tidal Studio, Perth WA.
  </div>
  <div class="lyrics">
    <div class="lyrics__col">
      <p>You're in an old photograph<br>Faded to grey before the night you turned your back<br>I can't undo that day<br>I felt my heart give way<br>Like frost it cracked and melted quietly</p>
      <p>Your words ran cold and deep<br>Left me to weep<br>Stripped of the things I'd keep<br>Your shadow stays with me<br>Sirens in the street as my heart it cries</p>
      <p>I hoped for a thunderstorm<br>I begged for the light<br>Not even the dawn could warm me</p>
      <p>And it's HOLLOWED to count the falling rain<br>HOLLOWED to call out your name<br>HOLLOWED I gotta find my tune<br>It's HOLLOWED I'm not saving my time for you</p>
      <p>Here comes another night<br>Tell me how many hours did I wait for you<br>These tears ring true<br>From dusk to morning I still stay<br>A stranger in my room for days, afraid<br>Because the world goes grey without you</p>
      <p>I taste the salt along my lips<br>Lost in this long eclipse</p>
    </div>
    <div class="lyrics__col">
      <p>The day will close without my closest friend<br>I hoped for a thunderstorm<br>I begged for the light<br>Not even the dawn could warm me</p>
      <p>And it's HOLLOWED to count the falling rain<br>HOLLOWED to call out your name<br>HOLLOWED I gotta find my tune<br>It's HOLLOWED I'm not saving my time for you</p>
      <p>Here comes another night<br>Tell me how many hours did I wait for you<br>These tears ring true<br>From dusk to morning I still stay<br>A stranger in my room for days, afraid<br>Because the world goes grey without you</p>
      <p>And it's HOLLOWED to count the falling rain<br>HOLLOWED to call out your name<br>HOLLOWED I gotta find my tune<br>It's HOLLOWED I'm not saving my time for you</p>
    </div>
  </div>
</section>
</div>
</body>
</html>
```